Specialty Plumbing Distributor Advertisement Flyer

We are looking to design a flyer to catch the eye of backflow preventer training schools and instructors and advertise a program we have here. Our company specializes in repair parts, tools, technical assistance etc. and through this no-cost program, we donate educational material to assist trainers for their classes. We offer coupons, store credit and free resources on website. It is called our “Keystone Mentor Initiative” and we also have a page on our website dedicated to the trainers we work with, where we send customers of ours that need backflow schooling.
Plumbing Training Schools
Education

```html
<!DOCTYPE html>
<html lang="en">
<head>
<meta charset="utf-8">
<title>Keystone Mentor Initiative Flyer</title>
<link rel="stylesheet" href="https://fonts.googleapis.com/css2?family=Montserrat:wght@300;400;700;800;900&family=Oswald:wght@500;600;700&family=Jost:wght@400;500&display=swap">
<style>
  :root {
    --red: #e21e26;
    --blue: #3d55a0;
    --blue-text: #34499b;
    --white: #ffffff;
    --ink: #2a2a2a;
    --silver-light: #e6e7e8;
    --silver-dark: #c4c6c9;
    --stage: #dcdcdc;
  }
  html, body {
    margin: 0;
    padding: 0;
    width: 1200px;
    height: 1200px;
    overflow: hidden;
    background: var(--stage);
  }
  .flyer {
    position: absolute;
    left: 204px;
    top: 40px;
    width: 792px;
    height: 1120px;
    display: block;
  }
  .band-title { font-family: "Montserrat", sans-serif; font-weight: 900; fill: var(--white); }
  .band-subtitle { font-family: "Montserrat", sans-serif; font-weight: 300; fill: var(--white); }
  .tagline-bold { font-family: "Montserrat", sans-serif; font-weight: 800; fill: var(--white); }
  .tagline-light { font-family: "Montserrat", sans-serif; font-weight: 400; fill: var(--white); }
  .tagline-light .strong { font-weight: 800; }
  .offer-heading { font-family: "Oswald", sans-serif; font-weight: 600; fill: var(--white); }
  .offer-item { font-family: "Montserrat", sans-serif; font-weight: 800; fill: var(--white); }
  .offer-item-light { font-family: "Montserrat", sans-serif; font-weight: 400; fill: var(--white); }
  .donate-heading { font-family: "Oswald", sans-serif; font-weight: 700; fill: var(--red); }
  .donate-line { font-family: "Jost", sans-serif; font-weight: 500; fill: var(--blue-text); }
  .products-intro { font-family: "Jost", sans-serif; font-weight: 500; fill: var(--blue-text); }
  .products-heading { font-family: "Oswald", sans-serif; font-weight: 700; fill: var(--red); }
  .product-item { font-family: "Jost", sans-serif; font-weight: 400; fill: var(--ink); font-size: 17px; }
  .product-star { fill: var(--blue); }
  .brand-name { font-family: "Jost", sans-serif; font-weight: 400; fill: var(--blue-text); }
  .contact-text { font-family: "Jost", sans-serif; font-weight: 500; fill: var(--white); font-size: 16px; }
</style>
</head>
<body>
<svg class="flyer" viewBox="0 0 891 1259" xmlns="http://www.w3.org/2000/svg" aria-label="Keystone Mentor Initiative flyer">
  <defs>
    <linearGradient id="silver" x1="0" y1="0" x2="1" y2="1">
      <stop offset="0" stop-color="var(--silver-dark)"/>
      <stop offset="0.5" stop-color="var(--silver-light)"/>
      <stop offset="1" stop-color="var(--silver-dark)"/>
    </linearGradient>
    <linearGradient id="classroom-tone" x1="0" y1="0" x2="1" y2="1">
      <stop offset="0" stop-color="#b9b3a6"/>
      <stop offset="0.5" stop-color="#c9bfae"/>
      <stop offset="1" stop-color="#a89c86"/>
    </linearGradient>
    <linearGradient id="workshop-tone" x1="0" y1="0" x2="1" y2="1">
      <stop offset="0" stop-color="#d8d6d2"/>
      <stop offset="1" stop-color="#8b8e93"/>
    </linearGradient>
    <linearGradient id="plant-tone" x1="0" y1="0" x2="1" y2="1">
      <stop offset="0" stop-color="#b6bcc2"/>
      <stop offset="0.55" stop-color="#d98040"/>
      <stop offset="1" stop-color="#5e6a76"/>
    </linearGradient>
    <linearGradient id="valve-tone" x1="0" y1="0" x2="0" y2="1">
      <stop offset="0" stop-color="#c8242b"/>
      <stop offset="0.3" stop-color="#d6b25a"/>
      <stop offset="1" stop-color="#a88a3c"/>
    </linearGradient>
    <linearGradient id="pump-tone" x1="0" y1="0" x2="1" y2="1">
      <stop offset="0" stop-color="#e0343a"/>
      <stop offset="1" stop-color="#a5161c"/>
    </linearGradient>
  </defs>

  <!-- Base surface -->
  <rect class="surface" x="0" y="0" width="891" height="1259" fill="url(#silver)"/>

  <!-- Photo areas -->
  <polygon class="photo-classroom" role="img" aria-label="Photo of a training classroom with two projector screens and tables of backflow parts"
           points="90,0 891,0 891,110 550,460" fill="url(#classroom-tone)"/>
  <polygon class="photo-workshop" role="img" aria-label="Photo of trainees practising on a backflow test wall"
           points="891,110 891,460 550,460" fill="url(#workshop-tone)"/>
  <line class="photo-divider" x1="891" y1="110" x2="550" y2="460" stroke="var(--silver-light)" stroke-width="6"/>
  <polygon class="photo-technician" role="img" aria-label="Photo of a technician in orange coveralls inspecting plant piping"
           points="0,180 312,492 0,805" fill="url(#plant-tone)"/>

  <!-- Red title band -->
  <polygon class="title-band" points="0,0 90,0 447.5,357.5 312,492 0,180" fill="var(--red)"/>
  <g transform="translate(90 0) rotate(45)">
    <text class="band-title" x="15" y="95" font-size="88" textLength="480" lengthAdjust="spacingAndGlyphs">KEYSTONE</text>
    <text class="band-subtitle" x="45" y="158" font-size="48" textLength="435" lengthAdjust="spacingAndGlyphs">MENTOR INITIATIVE</text>
  </g>

  <!-- White bottom panel -->
  <rect class="bottom-panel" x="0" y="962" width="891" height="297" fill="var(--white)"/>

  <!-- Blue tagline band -->
  <polygon class="tagline-band" points="447.5,357.5 532,442 13,962 0,962 0,805" fill="var(--blue)"/>
  <g transform="translate(0 805) rotate(-45)">
    <text class="tagline-bold" x="-20" y="55" font-size="23" textLength="600" lengthAdjust="spacingAndGlyphs">ENHANCE YOUR BACKFLOW TRAINING CLASSES</text>
    <text class="tagline-light" x="26" y="86" font-size="24" textLength="454" lengthAdjust="spacingAndGlyphs">WITH <tspan class="strong">FREE</tspan> EDUCATIONAL RESOURCES</text>
  </g>

  <!-- Offer card -->
  <g class="offer-card">
    <rect x="508" y="488" width="355" height="271" rx="14" fill="var(--red)"/>
    <path d="M522,488 H849 A14,14 0 0 1 863,502 V580 H508 V502 A14,14 0 0 1 522,488 Z" fill="var(--blue)"/>
    <rect x="518" y="498" width="335" height="251" rx="10" fill="none" stroke="var(--white)" stroke-width="1.6" stroke-dasharray="7 5"/>
    <text class="offer-heading" x="686" y="567" font-size="72" text-anchor="middle" textLength="280" lengthAdjust="spacingAndGlyphs">WE OFFER</text>
    <text class="offer-item" x="686" y="624" font-size="32" text-anchor="middle" textLength="196" lengthAdjust="spacingAndGlyphs">COUPONS</text>
    <line x1="555" y1="633" x2="817" y2="633" stroke="#f06a6f" stroke-width="1"/>
    <text class="offer-item" x="686" y="665" font-size="25" text-anchor="middle" textLength="196" lengthAdjust="spacingAndGlyphs">STORE CREDIT</text>
    <line x1="555" y1="675" x2="817" y2="675" stroke="#f06a6f" stroke-width="1"/>
    <text class="offer-item" x="686" y="702" font-size="21" text-anchor="middle" textLength="196" lengthAdjust="spacingAndGlyphs">FREE RESOURCES</text>
    <text class="offer-item-light" x="686" y="730" font-size="28" text-anchor="middle" textLength="196" lengthAdjust="spacingAndGlyphs">ON WEBSITE</text>
  </g>

  <!-- Valve product -->
  <rect class="product-valve" role="img" aria-label="Product photo of a brass pressure relief valve with red cap"
        x="215" y="760" width="62" height="172" rx="10" fill="url(#valve-tone)"/>

  <!-- Donation message -->
  <text class="donate-heading" x="408" y="870" font-size="100" textLength="455" lengthAdjust="spacingAndGlyphs">WE DONATE</text>
  <text class="donate-line" x="408" y="897" font-size="20" textLength="455" lengthAdjust="spacingAndGlyphs">EDUCATIONAL MATERIAL TO ASSIST TRAINERS</text>
  <text class="donate-line" x="408" y="942" font-size="48" textLength="455" lengthAdjust="spacingAndGlyphs">FOR THEIR CLASSES</text>

  <!-- Fire pump product -->
  <rect class="product-pump" role="img" aria-label="Product photo of a red electric fire pump assembly"
        x="56" y="970" width="280" height="180" rx="14" fill="url(#pump-tone)"/>

  <!-- Product list -->
  <text class="products-intro" x="841" y="1005" font-size="27" text-anchor="end" textLength="270" lengthAdjust="spacingAndGlyphs">THE PRODUCT TYPES</text>
  <text class="products-heading" x="395" y="1054" font-size="44" textLength="455" lengthAdjust="spacingAndGlyphs">WE WILL BE CARRYING ARE</text>

  <g class="product-list">
    <text class="product-star" x="474" y="1094" font-size="14">★</text>
    <text class="product-item" x="501" y="1094">Fire Pump repack kits</text>
    <text class="product-star" x="474" y="1125" font-size="14">★</text>
    <text class="product-item" x="501" y="1125">Fast Packs</text>
    <text class="product-star" x="474" y="1156" font-size="14">★</text>
    <text class="product-item" x="501" y="1156">Gland Bolt Assemblies</text>
    <text class="product-star" x="474" y="1187" font-size="14">★</text>
    <text class="product-item" x="501" y="1187">Lantern Rings</text>

    <text class="product-star" x="709" y="1090" font-size="14">★</text>
    <text class="product-item" x="736" y="1090">Case Gaskets</text>
    <text class="product-star" x="709" y="1121" font-size="14">★</text>
    <text class="product-item" x="736" y="1121">Packing</text>
    <text class="product-star" x="709" y="1152" font-size="14">★</text>
    <text class="product-item" x="736" y="1152">Bearings</text>
    <text class="product-star" x="709" y="1183" font-size="14">★</text>
    <text class="product-item" x="736" y="1183">Jockey Pumps</text>
  </g>

  <!-- Brand name -->
  <g class="brand">
    <rect x="46" y="1200" width="32" height="32" fill="var(--blue)"/>
    <text class="brand-name" x="92" y="1227" font-size="28">Liberty Flowline Supply Co.</text>
  </g>

  <!-- Contact strip -->
  <g class="contact-strip">
    <polygon points="428,1259 470,1212 891,1212 891,1259" fill="var(--blue)"/>
    <g class="icon-web" fill="none" stroke="var(--white)" stroke-width="1.4">
      <circle cx="498" cy="1237" r="11"/>
      <circle cx="498" cy="1237" r="7"/>
      <ellipse cx="498" cy="1237" rx="3.2" ry="7"/>
      <line x1="491" y1="1237" x2="505" y2="1237"/>
    </g>
    <text class="contact-text" x="518" y="1243">www.flowlineparts.com</text>
    <line x1="708" y1="1222" x2="708" y2="1252" stroke="var(--white)" stroke-width="1.5"/>
    <g class="icon-phone">
      <circle cx="730" cy="1237" r="11" fill="none" stroke="var(--white)" stroke-width="1.4"/>
      <path d="M725.5,1231.5 q1.5,-1.5 3,0 l1.2,2 q0.6,1.2 -0.6,2 q1.2,2.6 3.4,3.6 q0.8,-1.2 2,-0.6 l2,1.2 q1.5,1.5 0,3 q-2,1.6 -5,0 q-4.6,-2.6 -6.6,-6.6 q-1.4,-2.8 0.6,-4.6 z" fill="var(--white)"/>
    </g>
    <text class="contact-text" x="750" y="1243">800.555.0142</text>
  </g>
</svg>
</body>
</html>
```